Harrowgate Automotive Business Card

Automotive repair , all makes including Asian and European Imports. TQR Certified (Logo),fennlo (logo), Qwindle+ (logo)

Industry/Entity Type

Automotive

Contact Information for Business Card

Harrowgate Automotive, Carl Obrenski Owner, 3826 Poplar Rd. Larkfield, Mn 56390. Website harrowgateautomotive.com. (612) 555-0148

```html
<!DOCTYPE html>
<html lang="en">
<head>
<meta charset="utf-8">
<title>Harrowgate Automotive Business Card</title>
<link rel="stylesheet" href="https://fonts.googleapis.com/css2?family=Open+Sans:wght@400;600;700&display=swap">
<style>
  :root {
    --backdrop: #ecebe8;
    --card-white: #ffffff;
    --brand-blue: #1f3f9c;
    --brand-red: #d8232f;
    --ink: #1c1c1c;
    --band-grey: #bdbec0;
    --rule-grey: #9a9a9a;
    --engine-light: #b2b2b2;
    --engine-mid: #a2a2a2;
    --engine-dark: #939393;
    --tagline: #ffffff;
  }
  * { box-sizing: border-box; margin: 0; padding: 0; }
  html, body { width: 1200px; height: 1000px; overflow: hidden; }
  body {
    position: relative;
    background: var(--backdrop);
    font-family: "Open Sans", Arial, sans-serif;
    color: var(--ink);
  }
  .card {
    position: absolute;
    box-shadow: 0 3px 10px rgba(0,0,0,0.18);
    overflow: hidden;
  }
  /* Front card */
  .card-front {
    left: 78px; top: 189px; width: 370px; height: 621px;
    background: var(--card-white);
    text-align: center;
  }
  .wordmark {
    font-family: "Open Sans", Arial, sans-serif;
    font-weight: 700;
    color: var(--brand-blue);
    line-height: 1.05;
    letter-spacing: -0.5px;
  }
  .card-front .wordmark {
    position: absolute; left: 0; right: 0; top: 82px;
    font-size: 40px;
  }
  .person-name {
    position: absolute; left: 0; right: 0; top: 296px;
    font-size: 19px; font-weight: 700; color: var(--brand-blue);
  }
  .person-role {
    position: absolute; left: 0; right: 0; top: 322px;
    font-size: 15px; font-weight: 600; color: var(--brand-red);
    display: flex; justify-content: center; align-items: center; gap: 6px;
  }
  .person-role::before, .person-role::after {
    content: ""; width: 34px; height: 1px; background: var(--rule-grey);
  }
  .contact {
    position: absolute; left: 0; right: 0; top: 388px;
    font-size: 16px; line-height: 25px;
  }
  .contact .label { color: var(--brand-blue); font-weight: 700; }
  .address {
    position: absolute; left: 0; right: 0; top: 446px;
    font-size: 16px; line-height: 23px;
  }
  .social {
    position: absolute; left: 0; right: 0; top: 528px;
    display: flex; justify-content: center; gap: 14px;
    font-size: 12px; font-weight: 600;
  }
  .social-item { display: flex; align-items: center; gap: 5px; color: var(--brand-blue); }
  .social-item .dot { width: 16px; height: 16px; border-radius: 50%; background: var(--brand-blue); }
  .social-item.alt { color: var(--brand-red); }
  .social-item.alt .dot { background: var(--brand-red); }
  .cert-band {
    position: absolute; left: 0; right: 0; top: 559px; height: 32px;
    background: var(--band-grey);
    color: var(--brand-red); font-size: 14px; font-weight: 600;
    line-height: 32px;
  }
  /* Back cards */
  .card-back {
    left: 519px; width: 621px; height: 371px;
  }
  .card-back.top { top: 106px; }
  .card-back.bottom { top: 522px; }
  .engine-fill {
    position: absolute; inset: 0;
    background: radial-gradient(ellipse at 50% 40%, var(--engine-dark) 0%, var(--engine-mid) 55%, var(--engine-light) 100%);
  }
  .card-back .wordmark {
    position: absolute; left: 0; right: 0; text-align: center;
    font-size: 62px;
  }
  .card-back.top .wordmark { top: 108px; }
  .card-back.bottom .wordmark { top: 90px; }
  .tagline {
    position: absolute; left: 0; right: 0; top: 326px;
    text-align: center; color: var(--tagline);
    font-size: 14px; font-weight: 600; letter-spacing: 0.2px;
  }
</style>
</head>
<body>
  <section class="card card-front">
    <div class="wordmark">Harrowgate<br>Automotive</div>
    <div class="person-name">CARL OBRENSKI</div>
    <div class="person-role">Owner</div>
    <div class="contact">
      <div><span class="label">Tel:</span> (612) 555-0148</div>
      <div><span class="label">Web:</span> harrowgateautomotive.com</div>
    </div>
    <div class="address">3826 Poplar Rd. Larkfield<br>Mn 56390</div>
    <div class="social">
      <span class="social-item"><span class="dot"></span>fennlo</span>
      <span class="social-item alt"><span class="dot"></span>Qwindle+</span>
    </div>
    <div class="cert-band">TQR Certified</div>
  </section>

  <section class="card card-back top">
    <div class="engine-fill" role="img" aria-label="Faded grey photograph of a car engine bay"></div>
    <div class="wordmark">Harrowgate<br>Automotive</div>
  </section>

  <section class="card card-back bottom">
    <div class="engine-fill" role="img" aria-label="Faded grey photograph of a car engine bay"></div>
    <div class="wordmark">Harrowgate<br>Automotive</div>
    <div class="tagline">ALL MAKES INCLUDING ASIAN AND EUROPEAN IMPORTS</div>
  </section>
</body>
</html>
```